Redesign our App

We are looking for an experienced creative UI/UX designer to redesign our app to the best user experience possible.

You should redesign all the pages of the app.
Should use illustrative images.
Should use the same color scheme as our new logo. (Attached)

We have attached screenshots of our current app, also some images of inspirational designs.

```html
<!DOCTYPE html>
<html lang="en">
<head>
<meta charset="UTF-8">
<title>Claim Amount – Step 2</title>
<link rel="stylesheet" href="https://fonts.googleapis.com/css2?family=Montserrat:wght@500;600&display=swap">
<style>
  :root {
    --green: #3cb54a;
    --accent-red: #f15a47;
    --ink: #2b2d33;
    --surface: #ffffff;
    --chip: #f6f6f7;
    --ring: #eef5ef;
  }
  * { box-sizing: border-box; margin: 0; padding: 0; }
  html, body {
    width: 873px;
    height: 1200px;
    overflow: hidden;
    background: var(--surface);
    font-family: "Montserrat", sans-serif;
  }
  .screen {
    position: relative;
    width: 873px;
    height: 1200px;
    background: var(--surface);
  }
  .back-button {
    position: absolute;
    left: 67px;
    top: 106px;
    width: 46px;
    height: 46px;
    border-radius: 50%;
    background: var(--accent-red);
    display: flex;
    align-items: center;
    justify-content: center;
  }
  .balance-pill {
    position: absolute;
    right: 0;
    top: 69px;
    width: 245px;
    height: 50px;
    background: var(--green);
    border-radius: 14px 0 0 14px;
    color: #fff;
    font-weight: 600;
    font-size: 19px;
    display: flex;
    align-items: center;
    justify-content: center;
  }
  .points-pill {
    position: absolute;
    right: 0;
    top: 132px;
    width: 210px;
    height: 48px;
    background: var(--surface);
    border-radius: 14px 0 0 14px;
    box-shadow: 0 6px 14px rgba(0, 0, 0, 0.08);
    color: var(--green);
    font-weight: 600;
    font-size: 19px;
    display: flex;
    align-items: center;
    justify-content: center;
  }
  .stepper {
    position: absolute;
    top: 298px;
    left: 0;
    width: 100%;
    display: flex;
    justify-content: center;
    gap: 42px;
  }
  .step {
    width: 112px;
    height: 112px;
    border-radius: 50%;
    display: flex;
    align-items: center;
    justify-content: center;
    font-weight: 600;
    font-size: 23px;
  }
  .step--done {
    border: 3px solid var(--ring);
    color: var(--green);
    background: var(--surface);
  }
  .step--current {
    background: var(--green);
    color: #fff;
    box-shadow: 0 8px 16px rgba(60, 181, 74, 0.25);
  }
  .claim-title {
    position: absolute;
    top: 468px;
    width: 100%;
    text-align: center;
    font-weight: 600;
    font-size: 20px;
    color: var(--ink);
  }
  .claim-options {
    position: absolute;
    top: 527px;
    left: 0;
    width: 100%;
    display: flex;
    flex-direction: column;
    align-items: center;
    gap: 40px;
  }
  .claim-option {
    width: 294px;
    height: 71px;
    border-radius: 24px;
    background: var(--chip);
    display: flex;
    align-items: center;
    justify-content: center;
    font-weight: 500;
    font-size: 19px;
    color: var(--ink);
  }
</style>
</head>
<body>
  <main class="screen">
    <div class="back-button" aria-label="Back">
      <svg width="24" height="20" viewBox="0 0 24 20" aria-hidden="true">
        <path d="M21 10H4M10 3L3 10l7 7" fill="none" stroke="#fff" stroke-width="3.6" stroke-linecap="round" stroke-linejoin="round"/>
      </svg>
    </div>

    <div class="balance-pill">MVR 1,440.13</div>
    <div class="points-pill">227 points</div>

    <div class="stepper">
      <div class="step step--done">Step 1</div>
      <div class="step step--current">Step 2</div>
    </div>

    <h2 class="claim-title">Claim amount via:</h2>

    <div class="claim-options">
      <div class="claim-option">Via transfer receipt</div>
      <div class="claim-option">Via full ID name</div>
    </div>
  </main>
</body>
</html>
```